Vela Care is an innovative Australian Business offering organisations an online solution for depre

We need an extremely professional Business card that is positive as we offer engaging online technology to help with depression. Our target market is large scale adoption by major Organisations.The logo is supplied but font can alter .

We would like to see designs that use our logo on the front with altered font . Open to alteration on the sphere concept for the logo but happy with this and you may alter slightly if you wish.

back -displays contact details, with our names coloured in orange like the orange on our site . use creative flair

initial names to appear on cards are Sam Whitfield Director 0432516087 Sa.Whitfieldd@vela-care.com.au, www.vela-care.com.au

We are looking for fresh and professional designs with some creative flair.

i have attached a mock up of our site that should come across in the business card design...but
No images required from site

business card dimensions are 54x89. we will print logo in high gloss and card will be matt.

Target Market(s)

Large adoption by Doctors , Universities , not for profits and large organisations

Industry/Entity Type

Business

Requirements
Must have
• linkage to our site by way of design but no images needed from site except logo

Needs to be bright and vibrant in design as online tools for depression and anxiety . Also professional look.

```html
<!DOCTYPE html>
<html lang="en">
<head>
<meta charset="utf-8">
<title>Vela Care – Business Card</title>
<link rel="stylesheet" href="https://fonts.googleapis.com/css2?family=Open+Sans:wght@400;600&display=swap">
<style>
  :root {
    --bg: #e4e5e7;
    --card: #ffffff;
    --orange: #f2691a;
    --orange-light: #f8873a;
    --green: #2f8a3c;
    --grey-text: #555a5e;
    --panel: #0c0c0c;
    --panel-text: #e9e9e9;
  }
  * { box-sizing: border-box; margin: 0; padding: 0; }
  html, body { width: 1200px; height: 1000px; overflow: hidden; }
  body {
    background: radial-gradient(ellipse at 50% 40%, #f1f2f3 0%, var(--bg) 70%);
    font-family: "Open Sans", Arial, sans-serif;
    position: relative;
  }
  .card {
    position: absolute;
    width: 534px;
    height: 324px;
    background: var(--card);
    box-shadow: 0 8px 24px rgba(0,0,0,0.18);
    overflow: hidden;
  }
  .card--front { left: 600px; top: 110px; }
  .card--back { left: 70px; top: 560px; }

  .band {
    position: absolute;
    left: 0; right: 0;
    background: linear-gradient(180deg, var(--orange-light), var(--orange));
  }
  .band::before {
    content: "";
    position: absolute;
    left: 0; right: 0; top: -7px;
    height: 2px;
    background: var(--orange);
  }
  .card--front .band { top: 214px; height: 70px; }
  .card--back .band { top: 258px; height: 46px; }

  .brand {
    position: absolute;
    left: 0; right: 0; top: 150px;
    text-align: center;
  }
  .brand__name {
    font-size: 34px;
    font-weight: 400;
    color: var(--grey-text);
    letter-spacing: 0.5px;
  }

  .person { position: absolute; left: 40px; top: 58px; color: var(--green); }
  .person__name { font-size: 31px; font-weight: 600; line-height: 1.1; }
  .person__role { font-size: 18px; font-weight: 600; margin-top: 6px; }

  .contact {
    position: absolute;
    left: 22px; top: 200px;
    width: 278px; height: 110px;
    background: var(--panel);
    padding: 16px 14px;
    list-style: none;
    display: flex;
    flex-direction: column;
    justify-content: space-between;
  }
  .contact__item {
    display: flex;
    align-items: center;
    gap: 10px;
    color: var(--panel-text);
    font-size: 12.5px;
    white-space: nowrap;
  }
  .contact__icon { width: 12px; height: 12px; flex: none; }
</style>
</head>
<body>
  <section class="card card--front" aria-label="Card front">
    <div class="brand">
      <span class="brand__name">Vela Care</span>
    </div>
    <div class="band"></div>
  </section>

  <section class="card card--back" aria-label="Card back">
    <div class="person">
      <h1 class="person__name">Sam Whitfield</h1>
      <p class="person__role">Director</p>
    </div>
    <div class="band"></div>
    <ul class="contact">
      <li class="contact__item">
        <svg class="contact__icon" viewBox="0 0 12 12"><path d="M1 4 Q6 0 11 4 L9 5 L8 4 Q6 3 4 4 L3 5 Z M3 6 H9 L10 11 H2 Z" fill="#e9e9e9"/></svg>
        0432516087
      </li>
      <li class="contact__item">
        <svg class="contact__icon" viewBox="0 0 12 12"><circle cx="6" cy="6" r="2.2" fill="none" stroke="#e9e9e9" stroke-width="1.2"/><path d="M8.2 4 V7.3 Q8.2 8.6 9.6 8 Q11 7 10.6 5 Q10 1.3 6 1.3 Q1.3 1.3 1.3 6 Q1.3 10.7 6 10.7 Q7.5 10.7 8.6 10" fill="none" stroke="#e9e9e9" stroke-width="1.2"/></svg>
        Sa.Whitfieldd@vela-care.com.au
      </li>
      <li class="contact__item">
        <svg class="contact__icon" viewBox="0 0 12 12"><rect x="1" y="1.5" width="10" height="7" fill="none" stroke="#e9e9e9" stroke-width="1.2"/><path d="M4 11 H8 M6 8.5 V11" stroke="#e9e9e9" stroke-width="1.2"/></svg>
        www.vela-care.com.au
      </li>
    </ul>
  </section>
</body>
</html>
```